Update the A4 Specials Page for Restaurant/Cafe

Provide a MINIMALIST attractive Specials page we can print weekly for our food and drink specials to give to our guests. Final design is to be provided in WORD Document so it can be easily edited by Manager. Should be black text and MINIMALIST to minimise ink usage as we print hundreds a week. We have UPLOADED the existing page as a template for you to update. Maybe logo can stay, see what you think. Or delete it and do something else. Keep it simple. Choose a good FONT. Could be a little playful with a cocktail ICON or something. Our existing menus can be seen at www.tallpinebistro.com.au and they are using font Alegreya. Please note we are unable to provide any feedback to designers, however we really do appreciate your time if you are submitting a design. Thank you for your participation.

```html
<!DOCTYPE html>
<html lang="en">
<head>
<meta charset="utf-8">
<title>Tall Pine Bistro – Weekly Specials</title>
<link href="https://fonts.googleapis.com/css2?family=Bebas+Neue&family=Montserrat:wght@500;600;700;800&display=swap" rel="stylesheet">
<style>
  :root {
    --page: #ffffff;
    --ink: #111111;
    --panel-line: #b05a27;
    --sketch-tint: #fdf5ef;
    --icon-slot: #f6e9df;
  }
  * { margin: 0; padding: 0; box-sizing: border-box; }
  html, body { width: 920px; height: 1200px; overflow: hidden; background: var(--page); }
  .specials-page {
    position: relative;
    width: 920px;
    height: 1200px;
    background: var(--page);
    font-family: "Montserrat", Arial, sans-serif;
    color: var(--ink);
  }
  .side-artwork {
    position: absolute;
    top: 45px;
    height: 1100px;
    background: linear-gradient(180deg, #ffffff 0%, var(--sketch-tint) 50%, #ffffff 100%);
  }
  .side-artwork--left { left: 0; width: 150px; }
  .side-artwork--right { right: 0; width: 148px; }
  .brand-name {
    position: absolute;
    top: 86px;
    left: 0;
    width: 920px;
    text-align: center;
    font-weight: 800;
    font-size: 34px;
    line-height: 1;
    letter-spacing: 1px;
    color: var(--ink);
  }
  .specials-panel { position: absolute; inset: 0; }
  .specials-title {
    position: absolute;
    top: 244px;
    left: 0;
    width: 920px;
    text-align: center;
    font-family: "Bebas Neue", Impact, sans-serif;
    font-weight: 400;
    font-size: 60px;
    line-height: 1;
    letter-spacing: 0.5px;
  }
  .special { position: absolute; left: 214px; width: 350px; }
  .special__name { font-size: 26px; font-weight: 500; letter-spacing: 0.6px; line-height: 1; }
  .special__detail { font-size: 15.5px; font-weight: 600; line-height: 19px; }
  .special__price { font-size: 25px; font-weight: 700; line-height: 1; }
  .icon { position: absolute; }
  .icon-slot { position: absolute; background: var(--icon-slot); border-radius: 50%; }
</style>
</head>
<body>
<main class="specials-page">
  <div class="side-artwork side-artwork--left" role="img" aria-label="Faint line sketch of cocktails and fruit"></div>
  <div class="side-artwork side-artwork--right" role="img" aria-label="Faint line sketch of cocktails and fruit"></div>

  <h1 class="brand-name">TALL PINE BISTRO</h1>

  <section class="specials-panel">
    <svg width="920" height="1200" style="position:absolute;inset:0" aria-hidden="true">
      <path fill="var(--page)" stroke="var(--panel-line)" stroke-width="3" d="M290 204 C420 196,560 205,680 225 C760 240,770 300,768 380 C762 600,770 850,772 1010 C774 1100,700 1125,560 1122 C420 1120,330 1145,240 1130 C165 1118,160 1060,160 980 C162 750,158 500,150 380 C148 260,210 210,290 204 Z"/>
    </svg>

    <h2 class="specials-title">WEEKLY SPECIALS</h2>

    <article class="special" style="top:354px">
      <h3 class="special__name">CHICKEN FILO</h3>
      <p class="special__detail" style="margin-top:9px">Creamy Chicken with Pinenuts,<br>wrapped in Filo Pastry.</p>
      <p class="special__detail" style="margin-top:9px">Served with Side Salad &amp; Zulu Sauce</p>
      <p class="special__price" style="margin-top:12px">$24</p>
    </article>
    <div class="icon-slot" role="img" aria-label="Line icon of a chicken" style="left:574px;top:356px;width:118px;height:124px"></div>

    <article class="special" style="top:538px">
      <h3 class="special__name">MINESTRONE SOUP</h3>
      <p class="special__detail" style="margin-top:9px">Served with Garlic Bread</p>
      <p class="special__price" style="margin-top:14px">$8</p>
    </article>
    <svg class="icon" style="left:560px;top:512px" width="145" height="135" viewBox="0 0 145 135" fill="none" stroke="var(--ink)" stroke-width="3" stroke-linecap="round" stroke-linejoin="round" aria-hidden="true">
      <path d="M60 4 q-5 6 0 12 q5 6 0 12 M72 4 q-5 6 0 12 q5 6 0 12 M84 4 q-5 6 0 12 q5 6 0 12"/>
      <path d="M95 50 L122 12"/>
      <ellipse cx="72" cy="62" rx="68" ry="16"/>
      <path d="M4 64 C8 100,40 118,72 118 C104 118,136 100,140 64"/>
      <path d="M14 80 C24 100,46 108,72 108"/>
      <path d="M52 116 v14 h40 v-14"/>
      <circle cx="30" cy="60" r="3"/><circle cx="58" cy="56" r="3"/><circle cx="112" cy="58" r="3"/>
      <path d="M42 56 l8 0 l-4 7 z M92 54 l8 0 l-4 7 z"/><rect x="70" y="56" width="6" height="6"/>
    </svg>

    <article class="special" style="top:706px">
      <h3 class="special__name">COCKTAIL SPECIAL</h3>
      <p class="special__detail" style="margin-top:9px">PASSIONISTA</p>
      <p class="special__detail" style="margin-top:10px">Vodka, Passionfruit Pulp, Mango Puree</p>
      <p class="special__detail" style="margin-top:4px">Top up with Ginger &amp; Lemon Kombucha</p>
      <p class="special__price" style="margin-top:10px">$17</p>
    </article>
    <svg class="icon" style="left:563px;top:696px" width="140" height="132" viewBox="0 0 140 132" fill="none" stroke="var(--ink)" stroke-width="3" stroke-linecap="round" stroke-linejoin="round" aria-hidden="true">
      <path d="M36 4 A30 30 0 0 0 8 48 Z"/>
      <path d="M36 4 L22 26 M8 48 L22 26 M16 14 L22 26"/>
      <path d="M40 38 H130 L82 90 Z"/>
      <path d="M82 90 V124 M62 126 H102"/>
      <path d="M88 66 L130 20"/>
      <circle cx="74" cy="32" r="1.5"/>
    </svg>

    <article class="special" style="top:893px">
      <h3 class="special__name">CRAFT BEER SPECIAL</h3>
      <p class="special__detail" style="margin-top:9px">CROOKED GECKO</p>
      <p class="special__detail" style="margin-top:3px">SUN BURST</p>
      <p class="special__detail" style="margin-top:1px">Tropical Pale Ale</p>
      <p class="special__detail" style="margin-top:1px">4.8% Alc.</p>
      <p class="special__price" style="margin-top:12px">$10</p>
    </article>
    <svg class="icon" style="left:570px;top:904px" width="126" height="130" viewBox="0 0 126 130" fill="none" stroke="var(--ink)" stroke-width="3" stroke-linejoin="round" aria-hidden="true">
      <path d="M28 4 H42 V30 C52 38,56 44,56 54 V124 H4 V54 C4 44,8 38,18 30 V4 Z"/>
      <path d="M24 14 H38"/>
      <rect x="18" y="70" width="24" height="40"/>
      <path d="M70 60 H122 C124 80,112 92,96 92 C80 92,68 80,70 60 Z"/>
      <path d="M72 68 H120"/>
      <path d="M96 92 V124 M84 124 H108"/>
    </svg>
  </section>
</main>
</body>
</html>
```